Quiet Harbor Monthly Newsletter

I would like to have some backgrounds designed for July - December. We would pay for each page seperately. Each month should be its own design so that we may pick the best month for each. You are welcome to submit as many designs as you like for months. Months with themes will rate higher, for example July can incorporate Independence Day, December Christmas Season/Yule/Hannukah/Holidays,October Halloween, November Thanksgiving, September Labor Day, August can be summer themed. I am attaching our newsletter that I would like the design to work around. This verbiage does not need to be on the page right now. We would like to have the verbiage for each month applied to that month on purchase. www.tolvanpower.example is our website. We love designs that stay with our colors and website theme.

Target Market(s)

Homeowners

Industry/Entity Type

Electrical Contractor

Requirements
Must have
• Monthly or Seasonal Themes

```html
<!DOCTYPE html>
<html lang="en">
<head>
<meta charset="utf-8">
<title>Quiet Harbor Monthly – Tolvan Power LLC</title>
<link href="https://fonts.googleapis.com/css2?family=Anton&family=Montserrat:ital,wght@0,400;0,500;0,600;0,700;1,400;1,500;1,600&display=swap" rel="stylesheet">
<style>
  :root{
    --red:#e3141b;
    --red-dark:#b80d12;
    --yellow:#f7e600;
    --ink:#1c1c1c;
    --white:#ffffff;
    --backdrop:#f1f1f1;
  }
  *{box-sizing:border-box;margin:0;padding:0}
  html,body{width:1200px;height:3000px;overflow:hidden;background:var(--backdrop)}
  body{font-family:"Montserrat",sans-serif;color:var(--ink)}
  .page{position:absolute;left:122px;top:0;width:955px;height:3000px;background:var(--white);box-shadow:0 10px 40px rgba(0,0,0,.18);overflow:hidden}
  .abs{position:absolute}

  /* header */
  .brand{left:46px;top:30px;width:150px;height:60px;display:flex;align-items:center;gap:10px}
  .brand-dot{width:16px;height:16px;border-radius:50%;background:var(--red);flex:none}
  .brand-name{font-weight:700;font-size:20px;line-height:1.05;color:var(--ink)}
  .contact{display:flex;align-items:center;gap:14px;font-size:16px;font-weight:500}
  .contact svg{flex:none}
  .contact.phone{font-size:26px;font-weight:500}
  .contact.address{font-size:15px;line-height:1.1;font-weight:600;letter-spacing:.3px}

  /* hero */
  .hero{left:0;top:80px;width:955px;height:1090px}
  .hero-kicker{left:0;width:955px;text-align:center;font-family:"Anton",sans-serif;letter-spacing:4px}
  .kicker-title{top:222px;color:var(--yellow);font-size:40px}
  .kicker-edition{top:282px;color:var(--white);font-size:30px;letter-spacing:3px}
  .hero-headline{left:0;width:955px;top:612px;text-align:center;font-family:"Anton",sans-serif;line-height:108px;font-size:118px;text-shadow:0 4px 10px rgba(0,0,0,.45);letter-spacing:-1px}
  .hero-headline .white{color:var(--white)}
  .hero-headline .red{color:var(--red);display:block}

  /* body copy */
  .greeting{left:62px;top:1192px;width:830px}
  .greeting h2{font-style:italic;font-weight:500;color:var(--red);font-size:31px;margin-bottom:14px}
  .greeting p{font-size:19.5px;line-height:28px}
  .issue{left:62px;top:1392px;width:830px}
  .issue h2{font-style:italic;font-weight:500;color:var(--red);font-size:31px;margin-bottom:6px}
  .issue ol{list-style:none;font-size:17px;line-height:29px}
  .issue li span{display:inline-block;width:56px}

  .articles{left:62px;top:1562px;width:840px;font-size:14.3px;line-height:23px}
  .articles h3{color:var(--red);font-size:14.3px;font-weight:700;margin-bottom:13px}
  .articles p{margin-bottom:15px;text-align:justify}
  .articles .sign{margin-bottom:11px}
  .articles .sign em{font-weight:700}
  .articles ul{list-style:none;margin-bottom:15px}
  .articles .closing{font-style:italic;font-weight:500}

  .cta{left:329px;top:2539px;width:298px;height:44px;border-radius:22px;background:var(--red);border:2px solid var(--red-dark);box-shadow:0 10px 12px -6px rgba(0,0,0,.35);color:var(--white);font-weight:700;font-size:28px;display:flex;align-items:center;justify-content:center}
  .follow{left:63px;top:2606px;font-size:14.3px;display:flex;align-items:center;gap:14px}
  .social{display:flex;gap:10px;font-weight:600;font-size:12.5px}
  .sign-off{left:62px;top:2644px;width:740px;font-size:14.3px;line-height:23px}
  .sign-off p{margin-bottom:14px}

  .closing-waves{left:0;top:2545px}
  .footer-text{left:62px;top:2872px;width:836px;font-size:9px;line-height:13px}
  .footer-text p{margin-bottom:4px}
</style>
</head>
<body>
<div class="page">

  <!-- Header -->
  <div class="abs brand"><span class="brand-dot"></span><span class="brand-name">Tolvan Power LLC</span></div>

  <div class="abs contact" style="left:383px;top:12px">
    <svg width="30" height="22" viewBox="0 0 30 22"><rect x="1.5" y="1.5" width="27" height="19" fill="none" stroke="#e3141b" stroke-width="2"/><path d="M2 3 L15 13 L28 3" fill="none" stroke="#e3141b" stroke-width="2"/></svg>
    info@tolvanpower.example
  </div>
  <div class="abs contact phone" style="left:661px;top:8px">
    <svg width="30" height="30" viewBox="0 0 24 24"><path d="M6.6 10.8a15 15 0 0 0 6.6 6.6l2.2-2.2c.3-.3.7-.4 1-.2 1.1.4 2.3.6 3.6.6.6 0 1 .4 1 1V20c0 .6-.4 1-1 1A17 17 0 0 1 3 4c0-.6.4-1 1-1h3.5c.6 0 1 .4 1 1 0 1.3.2 2.5.6 3.6.1.3 0 .7-.2 1z" fill="#e3141b"/></svg>
    555-014-2260
  </div>
  <div class="abs contact address" style="left:383px;top:57px">
    <svg width="28" height="36" viewBox="0 0 24 32"><path d="M12 1C6 1 1.5 5.5 1.5 11.3 1.5 19 12 31 12 31s10.5-12 10.5-19.7C22.5 5.5 18 1 12 1z" fill="#e3141b"/><circle cx="12" cy="11" r="4" fill="#fff"/></svg>
    <span>1480 LARKSPUR AVE<br>MILLBROOK, CO 80000</span>
  </div>
  <div class="abs contact" style="left:661px;top:66px">
    <svg width="28" height="28" viewBox="0 0 24 24" fill="none" stroke="#e3141b" stroke-width="1.5"><circle cx="12" cy="12" r="10"/><ellipse cx="12" cy="12" rx="4.5" ry="10"/><path d="M2 12h20M4 6.5h16M4 17.5h16"/></svg>
    www.tolvanpower.example
  </div>

  <!-- Hero -->
  <svg class="abs hero" viewBox="0 0 955 1090" role="img" aria-label="Photo of electrician's tools on a wooden workbench: wrench, pliers, tape measure, gloves, hard hat, face mask and an American flag">
    <defs>
      <linearGradient id="woodTone" x1="0" y1="0" x2="1" y2="1">
        <stop offset="0" stop-color="#7a4322"/>
        <stop offset=".45" stop-color="#5a2e16"/>
        <stop offset=".75" stop-color="#4a2612"/>
        <stop offset="1" stop-color="#2f1a10"/>
      </linearGradient>
      <linearGradient id="flagTone" x1="0" y1="0" x2="1" y2="0">
        <stop offset="0" stop-color="#a02a2a"/>
        <stop offset=".5" stop-color="#d9d4cf"/>
        <stop offset="1" stop-color="#2a3f7a"/>
      </linearGradient>
      <linearGradient id="bandRed" x1="0" y1="0" x2="1" y2="0">
        <stop offset="0" stop-color="#e3141b"/>
        <stop offset=".6" stop-color="#e3141b"/>
        <stop offset="1" stop-color="#f0527a"/>
      </linearGradient>
      <clipPath id="heroClip">
        <path d="M0 10 C120 70 260 100 420 80 C600 60 760 100 880 250 C920 300 940 320 955 330 L955 960 C820 990 700 1060 520 1072 C330 1085 180 980 0 890 Z"/>
      </clipPath>
    </defs>
    <g clip-path="url(#heroClip)">
      <rect width="955" height="1090" fill="url(#woodTone)"/>
      <path d="M0 860 C200 800 420 840 640 860 C780 874 900 900 955 880 L955 1090 L0 1090 Z" fill="url(#flagTone)" opacity=".85"/>
      <ellipse cx="900" cy="830" rx="120" ry="90" fill="#f1c51a" opacity=".9"/>
    </g>
    <path d="M0 0 C120 60 260 90 420 70 C600 50 770 95 890 240 C925 285 945 305 955 315 L955 335 C935 320 915 300 880 255 C760 105 600 65 420 85 C260 105 120 75 0 14 Z" fill="#e3141b"/>
    <path d="M0 880 C170 950 310 1040 500 1040 C680 1040 820 950 955 935 L955 990 C820 1000 690 1075 510 1082 C320 1090 170 1000 0 930 Z" fill="url(#bandRed)"/>
    <path d="M0 935 C170 1005 320 1095 510 1088 C690 1080 820 1000 955 990 L955 1090 L0 1090 Z" fill="#ffffff"/>
  </svg>

  <div class="abs hero-kicker kicker-title">QUIET HARBOR MONTHLY</div>
  <div class="abs hero-kicker kicker-edition">September 2024 Edition</div>
  <div class="abs hero-headline"><span class="white">WELCOME TO</span><span class="red">QUIET HARBOR</span><span class="white">MONTHLY!</span></div>

  <!-- Greeting -->
  <section class="abs greeting">
    <h2>Hello, valued clients and partners!</h2>
    <p>We are thrilled to welcome you to the inaugural issue of our monthly newsletter, designed to keep you informed about the latest trends, tips, and updates in the electrical contracting world. Whether you're a homeowner, business owner, or industry professional, there's something here for everyone.</p>
  </section>

  <section class="abs issue">
    <h2>In This Issue:</h2>
    <ol>
      <li><span>1.</span>A Warm Welcome from Our CEO</li>
      <li><span>2.</span>Project Spotlight: Green Energy Initiative</li>
      <li><span>3.</span>Safety First: Summer Electrical Safety Tips</li>
      <li><span>4.</span>Ask an Expert: Your Questions Answered</li>
    </ol>
  </section>

  <!-- Articles -->
  <section class="abs articles">
    <h3>1. A Warm Welcome from Our CEO</h3>
    <p>Greetings!</p>
    <p>I'm delighted to introduce you to our new monthly newsletter, Quiet Harbor Monthly. At Tolvan Power, we are committed to excellence, safety, and innovation in all our electrical projects. Through this newsletter, we aim to share our knowledge, celebrate our successes, and strengthen our relationship with you.</p>
    <p>I want to thank all of our clients for your business and your partnership. The journey has been amazing. We are thrilled to welcome you to the inaugural issue of our monthly newsletter, designed to keep you informed about the latest trends, tips, and updates in the electrical contracting world. Whether you're a homeowner, business owner, or industry professional, there's something here for everyone.</p>
    <p>I also wanted to introduce some new programs we are introducing. We are offering a Home Membership program [Link to the webpage], a referral program [Link to the webpage], and free video estimates [Link to the webpage]. We have started a non-profit aimed at helping lower-income households with electrical work that is hazardous at a discounted price or at no cost, on a case-by-case basis. This is in the beginning stages, and we will keep you updated as this progresses. Our non-profit is called Helping Circuits. Stay tuned for more updates!</p>
    <p class="sign"><em>Sincerely,</em><br>Daniel Ashford<br>CEO, Tolvan Power LLC</p>
    <h3>2. Project Spotlight: Green Energy Initiative</h3>
    <p>This month, we're excited to highlight our recent work on the Green Energy Initiative. Our team is currently replacing @ 400 fluorescent light fixtures with LEDs, significantly reducing this client's carbon footprint and energy costs. This project underscores our dedication to sustainable and environmentally friendly solutions.</p>
    <h3>3. Safety First: Summer Electrical Safety Tips</h3>
    <p style="margin-bottom:0">As temperatures rise, so does the risk of electrical hazards. Here are some tips to keep your home and workplace safe this summer:</p>
    <ul>
      <li>• Avoid Overloading Circuits: Ensure that air conditioners and other heavy-duty appliances are on separate circuits.</li>
      <li>• Inspect Electrical Cords: Replace any damaged or frayed cords immediately.</li>
      <li>• Stay Dry: Keep electrical devices away from water sources, especially pools and sprinklers.</li>
      <li>• Use GFCIs: Install Ground Fault Circuit Interrupters in areas prone to moisture to prevent shocks.</li>
    </ul>
    <p class="closing">Stay safe and enjoy a worry-free summer!</p>
    <h3>4. Ask an Expert: Your Questions Answered</h3>
    <p>Have questions about electrical systems, safety, or new technologies? Our experts are here to help! Send your questions to info@tolvanpower.example and we'll feature the answers in our next newsletter.</p>
  </section>

  <!-- Closing -->
  <svg class="abs closing-waves" width="955" height="455" viewBox="0 0 955 455" aria-hidden="true">
    <path d="M950 8 C860 60 760 150 690 230 C640 285 580 320 520 330 C600 300 650 260 700 210 C780 130 880 50 950 8 Z" fill="#e3141b"/>
    <path d="M0 330 L0 285 C120 235 300 225 460 240 C600 255 700 290 800 290 C860 290 910 280 955 268 L955 280 C880 300 790 305 690 295 C560 282 400 250 240 262 C140 270 60 300 0 330 Z" fill="#e3141b"/>
  </svg>

  <div class="abs cta">Stay Connected!</div>
  <div class="abs follow">Follow us on social media for the latest updates, tips, and promotions:
    <span class="social"><span>Snapline</span><span>Friendway</span><span>Chirper</span></span>
  </div>
  <div class="abs sign-off">
    <p>Thank you for reading Quiet Harbor Monthly. We look forward to bringing you more valuable insights and updates next month!</p>
    <p><strong>Best regards,</strong><br>The Team at Tolvan Power LLC<br>(555) 014-2260</p>
  </div>

  <div class="abs footer-text">
    <p><strong>Tolvan Power LLC</strong><br>Electrical Excellence. Unmatched Service.</p>
    <p>I want to thank all of our clients for your business and your partnership. The journey has been amazing. We are thrilled to welcome you to the inaugural issue of our monthly newsletter, designed to keep you informed about the latest trends, tips, and updates in the electrical contracting world. Whether you're a homeowner, business owner, or industry professional, there's something here for everyone.</p>
    <p>I also wanted to introduce some new programs we are introducing. We are offering a Home Membership program [Link to the webpage], a referral program [Link to the webpage], and free video estimates [Link to the webpage]. We have started a non-profit aimed at helping lower-income households with electrical work that is hazardous at a discounted price or at no cost, on a case-by-case basis. This is in the beginning stages, and we will keep you updated as this progresses. Our non-profit is called Helping Circuits. Stay tuned for more updates!</p>
  </div>

</div>
</body>
</html>
```